Medical equipment business looking for professional, unique business card

We need a business card design for a durable medical equipment company. We are small but would like our cards to express that we are much bigger. We focus on braces (back, knee, wrist, etc) but also do crutches, rollators, wheelchairs- basically medical equipment that gets you going and back in Stride. Our colors are blue and green and our logo has an arrow and use of a "spine". We'd like to express professionalism while being unique.

Industry/Entity Type

Medical Equipment

Contact Information for Business Card

Professional feel but unique. Memorable.

Font styles to use
Serif
Sans Serif
Other font styles liked:
• verdana

Requirements
Must have
• card holders cell#, business phone#, fax#, email, website address, business address, logo
Nice to have
• use of medical/healthcare related descriptive words, items, look
Should not have
• the wrong colors or cartoon characters.

```html
<!DOCTYPE html>
<html lang="en">
<head>
<meta charset="utf-8">
<title>Stride Medical – Business Card</title>
<link rel="stylesheet" href="https://fonts.googleapis.com/css2?family=Montserrat:wght@400;500;600&display=swap">
<style>
  :root {
    --navy: #0b4068;
    --green: #8dc63f;
    --page: #e6e7e8;
    --card: #ffffff;
  }
  * { margin: 0; padding: 0; box-sizing: border-box; }
  html, body { width: 1200px; height: 927px; overflow: hidden; background: var(--page); }
  body { position: relative; font-family: "Montserrat", sans-serif; color: var(--navy); }

  .card {
    position: absolute; left: 378px; top: 75px; width: 445px; height: 778px;
    background: var(--card); border-radius: 32px; overflow: hidden; text-align: center;
  }
  .brand {
    position: absolute; top: 100px; left: 0; width: 100%;
    display: flex; align-items: center; justify-content: center; gap: 12px;
  }
  .brand-dot { width: 22px; height: 22px; border-radius: 50%; background: var(--green); }
  .brand-name { font-size: 38px; font-weight: 600; color: var(--navy); letter-spacing: 0.5px; }

  .holder-name {
    position: absolute; top: 420px; width: 100%;
    font-size: 31px; font-weight: 500; color: var(--green); letter-spacing: 0.5px;
  }
  .holder-title { position: absolute; top: 456px; width: 100%; font-size: 18px; }

  .rule {
    position: absolute; left: 80px; width: 282px; height: 2px;
    background: linear-gradient(90deg, rgba(11,64,104,0.2), var(--navy) 20%, var(--navy) 80%, rgba(11,64,104,0.2));
  }
  .rule-top { top: 423px; }
  .rule-bottom { top: 666px; }

  .address { position: absolute; top: 437px; width: 100%; font-size: 19.5px; line-height: 24px; letter-spacing: 0.4px; }
  .icons { position: absolute; top: 503px; width: 100%; display: flex; justify-content: center; gap: 8px; }
  .icons svg { width: 14px; height: 14px; stroke: var(--green); fill: none; stroke-width: 1.4; }
  .contact { position: absolute; top: 533px; width: 100%; font-size: 19.5px; line-height: 24.2px; letter-spacing: 0.4px; }
  .contact .accent { color: var(--green); }
  .tagline { position: absolute; top: 688px; width: 100%; font-size: 18px; line-height: 23px; letter-spacing: 0.3px; }

  .band { position: absolute; top: 745px; height: 33px; }
  .band-left { left: 0; width: 68px; background: var(--green); }
  .band-mid { left: 72px; width: 300px; background: var(--navy); }
  .band-right { left: 376px; width: 69px; background: var(--green); }

  /* rules positioned relative to card: rule-top at card y 423 after name */
</style>
</head>
<body>
  <div class="card">
    <div class="brand">
      <span class="brand-dot"></span>
      <span class="brand-name">Stride Medical</span>
    </div>

    <div class="holder-name" style="top:347px">Marcus Hale</div>
    <div class="holder-title" style="top:383px">Director</div>

    <div class="rule rule-top"></div>

    <div class="address">450 Harbor Lane Suite 210<br>Cedarville, GA 30418</div>

    <div class="icons" aria-label="Mobile, phone, fax, email, web">
      <svg viewBox="0 0 14 14"><rect x="3.5" y="1" width="7" height="12" rx="1"/><line x1="6" y1="11" x2="8" y2="11"/></svg>
      <svg viewBox="0 0 14 14"><path d="M3 1.5l2 0.5 0.8 2.8-1.3 1c0.8 1.8 2 3 3.7 3.7l1-1.3 2.8 0.8 0.5 2c-6 1-10-3-9.5-9.5z"/></svg>
      <svg viewBox="0 0 14 14"><rect x="1" y="5" width="12" height="5" rx="1"/><rect x="4" y="2" width="6" height="3"/><rect x="4" y="8.5" width="6" height="4"/></svg>
      <svg viewBox="0 0 14 14"><rect x="1" y="3" width="12" height="8" rx="1"/><path d="M1 3.5l6 4.5 6-4.5"/></svg>
      <svg viewBox="0 0 14 14"><circle cx="7" cy="7" r="5.8"/><ellipse cx="7" cy="7" rx="2.6" ry="5.8"/><line x1="1.2" y1="7" x2="12.8" y2="7"/><line x1="2" y1="4.2" x2="12" y2="4.2"/><line x1="2" y1="9.8" x2="12" y2="9.8"/></svg>
    </div>

    <div class="contact">
      +330 5128 4417<br>
      +330 5128 4420<br>
      +003 7745 3902<br>
      info@stridemed.com<br>
      www.<span class="accent">stridemed</span>.com
    </div>

    <div class="rule rule-bottom"></div>

    <div class="tagline">Medical equipment that gets<br>you going and back in Stride</div>

    <div class="band band-left"></div>
    <div class="band band-mid"></div>
    <div class="band band-right"></div>
  </div>
</body>
</html>
```